Interior design service, along with home organization, packing, and staging, home and business. As well as staging in conjunction with real estate sales.

Love many of your designs and will be choosing today. To inform you of the exact details needed, the name of the company is "Flourish by Marnie T" , my phone number and e-,ail need to be included. i also need either description or some sort of bullet points that give an idea of the following:

- Interior design for home and business
- Home organization and packing
- Staging for personal and professional space
- Real estate stagingĀ 

Thank you

Target Market(s)

wide audience, but most importantly people looking for a quality service

Industry/Entity Type

Real Estate

Contact Information for Business Card

Flourish By Marnie T
Marnie Toller
(555)617-3942
mtbriar@inboxly.example

Requirements
Must have
• I'm 29 so i want my card to reflect something professional but still fresh. I don't have any specific photos or quotes that Ive included, however I like the card to reflect a personal touch, which is what I'm seeking from this service in the design of my card. Thanks!

```html
<!DOCTYPE html>
<html lang="en">
<head>
<meta charset="utf-8">
<title>Flourish By Marnie T — Business Card</title>
<link rel="stylesheet" href="https://fonts.googleapis.com/css2?family=Open+Sans:wght@400&display=swap">
<style>
  :root {
    --page-bg: #1c1511;
    --brand-blue: #5aaee3;
    --card-deep: #3a0f05;
    --card-mid: #7a2c0e;
    --card-glow: #a4521f;
    --ink-white: #ffffff;
    --band-white: #ffffff;
  }
  * { margin: 0; padding: 0; box-sizing: border-box; }
  html, body {
    width: 927px; height: 1200px; overflow: hidden;
    background: var(--page-bg);
    font-family: "Open Sans", Arial, sans-serif;
  }
  .sheet { position: relative; width: 927px; height: 1200px; }

  .brand-header {
    position: absolute; left: 0; top: 18px; width: 927px;
    text-align: center; color: var(--brand-blue);
  }
  .brand-header .name-main { font-size: 96px; line-height: 1.1; letter-spacing: 1px; }
  .brand-header .name-sub { font-size: 26px; letter-spacing: 1.5px; margin-top: -4px; padding-left: 250px; }

  .card {
    position: absolute; top: 184px; width: 400px; height: 234px; overflow: hidden;
    background: radial-gradient(ellipse at 50% 50%, var(--card-glow) 0%, var(--card-mid) 45%, var(--card-deep) 100%);
  }
  .card-front { left: 59px; }
  .card-back { left: 475px; width: 402px;
    background: radial-gradient(ellipse at 50% 75%, var(--card-glow) 0%, var(--card-mid) 50%, var(--card-deep) 100%); }

  .front-name {
    position: absolute; left: 0; top: 72px; width: 100%;
    text-align: center; color: var(--brand-blue);
  }
  .front-name .name-main { font-size: 50px; line-height: 1.1; }
  .front-name .name-sub { font-size: 13px; letter-spacing: 1px; padding-left: 140px; }

  .back-band {
    position: absolute; left: 0; top: 78px; width: 100%; height: 13px;
    background: var(--band-white);
    border-top: 2px solid var(--brand-blue);
    border-bottom: 2px solid var(--brand-blue);
  }
  .back-name {
    position: absolute; left: 24px; top: 36px;
    color: var(--brand-blue); font-size: 30px; line-height: 1.2;
  }
  .services {
    position: absolute; left: 0; top: 98px; width: 100%;
    list-style: none; text-align: center;
    color: var(--brand-blue); font-size: 11.5px; line-height: 12.5px;
  }
  .contact {
    position: absolute; right: 19px; top: 156px; text-align: right;
    color: var(--ink-white); font-size: 11px; line-height: 14px;
  }
  .contact .person { color: var(--brand-blue); font-size: 17px; line-height: 22px; }
  .contact .email { font-size: 9.5px; }
</style>
</head>
<body>
<main class="sheet">
  <header class="brand-header">
    <div class="name-main">Flourish</div>
    <div class="name-sub">By Marnie T</div>
  </header>

  <section class="card card-front" aria-label="Card front">
    <div class="front-name">
      <div class="name-main">Flourish</div>
      <div class="name-sub">By Marnie T</div>
    </div>
  </section>

  <section class="card card-back" aria-label="Card back">
    <div class="back-name">Flourish By Marnie T</div>
    <div class="back-band"></div>
    <ul class="services">
      <li>- Interior Design for Home and Business</li>
      <li>- Home Organization and Packing</li>
      <li>- Staging for Personal and Professional Space</li>
      <li>- Real Estate Staging</li>
    </ul>
    <div class="contact">
      <div class="person">Marnie Toller</div>
      <div class="phone">Phone (555)617-3942</div>
      <div class="email">mtbriar@inboxly.example</div>
    </div>
  </section>
</main>
</body>
</html>
```